Lanternleaf - Fresh Asian Cuisine Menu

We need to redo our menu to include pictures of food items. Our restaurant is vibrant, trendy, upscale Chinese cuisine

Requirements
Must have
• Must fit on 8.5x11 paper. We can remove the About Us section if needed but menu cannot be more than 6 pages total. Must include pictures of menu items

```html
<!DOCTYPE html>
<html lang="en">
<head>
<meta charset="utf-8">
<title>Lanternleaf - Fresh Asian Cuisine Menu</title>
<link href="https://fonts.googleapis.com/css2?family=Source+Serif+4:opsz,wght@8..60,400;8..60,500;8..60,600&display=swap" rel="stylesheet">
<style>
  :root {
    --backdrop: #ececec;
    --page: #f4f4f4;
    --page-shade: #e6e6e6;
    --ink: #2a2a2a;
    --ink-soft: #4a4a4a;
    --menu-red: #c8272b;
    --mat-red: #d33a3a;
    --plate: #ffffff;
  }
  * { box-sizing: border-box; margin: 0; padding: 0; }
  html, body { width: 1200px; height: 960px; overflow: hidden; }
  body { background: var(--backdrop); font-family: "Source Serif 4", Georgia, serif; color: var(--ink); }

  .spread { position: absolute; left: 30px; top: 111px; width: 1140px; height: 738px; display: flex; box-shadow: 0 10px 30px rgba(0,0,0,.18); }
  .page { position: relative; width: 570px; height: 738px; overflow: hidden; background: linear-gradient(90deg, var(--page) 0%, #fafafa 60%, var(--page-shade) 100%); }
  .page--left { border-left: 6px solid var(--menu-red); }
  .page--right { background: linear-gradient(90deg, var(--page-shade) 0%, #fafafa 12%, var(--page) 100%); border-right: 6px solid var(--menu-red); }

  .photo { position: absolute; }
  .photo--round { border-radius: 50%; border: 12px solid var(--plate); box-shadow: 0 4px 10px rgba(0,0,0,.15); }
  .photo--plate { border-radius: 10px; border: 10px solid var(--plate); box-shadow: 0 4px 10px rgba(0,0,0,.15); }
  .mat { position: absolute; background: var(--mat-red); }

  .menu-item { position: absolute; width: 150px; z-index: 5; }
  .menu-item h3 { font-size: 12px; font-weight: 500; line-height: 1.05; margin-bottom: 2px; }
  .menu-item p { font-size: 8px; line-height: 1.4; color: var(--ink-soft); }
  .menu-item .extra { display: block; text-align: right; font-weight: 600; color: var(--ink); }

  .chev { position: absolute; z-index: 5; width: 6px; height: 6px; border-right: 1.4px solid var(--ink); border-bottom: 1.4px solid var(--ink); }
  .chev--right { transform: rotate(-45deg); }
  .chev--left { transform: rotate(135deg); }
  .chev--up { transform: rotate(-135deg); }
  .chev--down { transform: rotate(45deg); }
</style>
</head>
<body>
<main class="spread">

  <section class="page page--left">
    <div class="mat" style="left:-30px; top:390px; width:390px; height:270px; transform:rotate(8deg);"></div>

    <div class="photo photo--plate" role="img" aria-label="Scallion pancakes folded on a white plate" style="left:11px; top:0; width:237px; height:161px; background:linear-gradient(135deg,#e8c489,#c99553);"></div>
    <div class="photo" role="img" aria-label="Dried red chili peppers" style="left:250px; top:18px; width:76px; height:84px; border-radius:40%; background:linear-gradient(135deg,#b0231c,#7a140f);"></div>
    <div class="photo" role="img" aria-label="Folded linen napkin" style="left:260px; top:110px; width:95px; height:205px; background:#e3dccd; transform:rotate(6deg);"></div>
    <div class="photo" role="img" aria-label="Buddha bang shrimp over shredded cabbage in a red bowl" style="left:329px; top:-24px; width:236px; height:236px; border-radius:50%; border:14px solid #c81d1d; background:radial-gradient(circle,#e49a45 0%,#d9c9a6 70%);"></div>
    <div class="photo" role="img" aria-label="Garlic cucumber salad in a dark square dish" style="left:-6px; top:228px; width:173px; height:242px; border-radius:10px; background:linear-gradient(135deg,#3f6a2c,#8fbc5a 50%,#2b2b2b);"></div>
    <div class="photo photo--plate" role="img" aria-label="Pan fried chicken dumplings on a white plate" style="left:337px; top:224px; width:224px; height:175px; transform:rotate(-8deg); background:linear-gradient(135deg,#eed49a,#c99a55);"></div>
    <div class="photo" role="img" aria-label="Wooden spoon" style="left:503px; top:376px; width:34px; height:188px; border-radius:17px 17px 6px 6px; background:linear-gradient(90deg,#a77b4f,#d4ab7c);"></div>
    <div class="photo photo--round" role="img" aria-label="Drunken chicken in chili sauce in a white bowl" style="left:174px; top:398px; width:188px; height:188px; background:radial-gradient(circle,#b8562b 0%,#8f2312 70%);"></div>
    <div class="photo photo--round" role="img" aria-label="Sichuan spiced beef with cilantro on a white plate" style="left:-70px; top:490px; width:250px; height:250px; background:radial-gradient(circle,#b46b2d 0%,#5e7f2d 65%);"></div>
    <div class="photo" role="img" aria-label="West Lake soup in a stoneware bowl" style="left:333px; top:537px; width:232px; height:232px; border-radius:50%; border:14px solid #8e7a55; background:radial-gradient(circle,#cfc6b4 0%,#9c8d72 80%);"></div>

    <span class="chev chev--up" style="left:68px; top:165px;"></span>
    <article class="menu-item" style="left:63px; top:177px;">
      <h3>Scallion Pancakes</h3>
      <p>Traditional Chinese flatbread folded with oil and minced scallions and pan fried</p>
    </article>

    <article class="menu-item" style="left:227px; top:176px; width:130px;">
      <h3>Buddha Bang Shrimp</h3>
      <p>Crispy fried shrimp tossed in our creamy spicy sauce</p>
    </article>
    <span class="chev chev--right" style="left:357px; top:190px;"></span>

    <span class="chev chev--left" style="left:188px; top:246px;"></span>
    <article class="menu-item" style="left:202px; top:244px; width:125px;">
      <h3>Garlic Cucumber Salad</h3>
      <p>Sliced cucumber with a garlic vinaigrette</p>
    </article>

    <article class="menu-item" style="left:202px; top:301px; width:125px;">
      <h3>Fried Chicken Dumplings (6)</h3>
      <p>Chinese dumpling stuffed with Chicken, Shiitake mushrooms and bamboo shoots scallions and pan fried</p>
    </article>
    <span class="chev chev--right" style="left:324px; top:316px;"></span>

    <article class="menu-item" style="left:388px; top:425px; width:115px;">
      <h3>Edamame</h3>
      <p>Seasoned &amp; boiled soy bean</p>
    </article>

    <article class="menu-item" style="left:389px; top:465px; width:115px;">
      <h3>West Lake Soup</h3>
      <p>Light creamy soup with ground beef, diced Shiitake mushroom, tofu, bamboo shoots, egg white and cilantro</p>
    </article>
    <span class="chev chev--down" style="left:391px; top:528px;"></span>

    <span class="chev chev--up" style="left:240px; top:616px;"></span>
    <article class="menu-item" style="left:200px; top:628px; width:125px;">
      <h3>Drunken Chicken</h3>
      <p>Chicken, Thai chili in a house made spicy sauce</p>
    </article>

    <span class="chev chev--left" style="left:188px; top:683px;"></span>
    <article class="menu-item" style="left:200px; top:680px; width:125px;">
      <h3>Sichuan Spiced Beef</h3>
      <p>Beef Shank, beef tripe, cilantro, peanuts and celery</p>
    </article>
  </section>

  <section class="page page--right">
    <div class="mat" style="left:183px; top:-6px; width:230px; height:40px; transform:rotate(-3deg);"></div>
    <div class="mat" style="left:-20px; top:590px; width:620px; height:180px; transform:rotate(-6deg);"></div>

    <div class="photo photo--plate" role="img" aria-label="Crispy mala beef jerky with dried chili on a white plate" style="left:9px; top:0; width:201px; height:175px; background:radial-gradient(circle,#5a2a24 0%,#2d1512 80%);"></div>
    <div class="photo" role="img" aria-label="Bamboo mat" style="left:413px; top:103px; width:160px; height:72px; background:repeating-linear-gradient(90deg,#d9d4bd 0 6px,#c4bd9f 6px 8px);"></div>
    <div class="photo photo--round" role="img" aria-label="Beef crispy bottom bao buns on a white plate" style="left:389px; top:-18px; width:180px; height:180px; background:radial-gradient(circle,#f2e7cf 0%,#dccaa2 80%);"></div>
    <div class="photo" role="img" aria-label="Fresh red chili peppers" style="left:350px; top:192px; width:56px; height:70px; border-radius:40%; background:linear-gradient(135deg,#c0231a,#7d120c);"></div>
    <div class="photo photo--round" role="img" aria-label="Red oil dumplings in Sichuan chili sauce" style="left:201px; top:190px; width:150px; height:150px; background:radial-gradient(circle,#e6b463 0%,#b8361d 70%);"></div>
    <div class="photo" role="img" aria-label="Hot and sour soup in a wooden bowl" style="left:358px; top:200px; width:260px; height:260px; border-radius:50%; border:16px solid #8a4a26; background:radial-gradient(circle,#e07a2e 0%,#b4431a 80%);"></div>
    <div class="photo photo--plate" role="img" aria-label="Lettuce wraps with seasoned ground chicken" style="left:9px; top:318px; width:170px; height:236px; transform:rotate(3deg); background:linear-gradient(180deg,#cfe2b0 0%,#a9c98a 38%,#3a2f24 42%,#8a6a3e 100%);"></div>
    <div class="photo" role="img" aria-label="Shredded carrots" style="left:331px; top:416px; width:103px; height:116px; border-radius:45%; background:radial-gradient(circle,#f5a531 0%,rgba(245,165,49,0) 75%);"></div>
    <div class="photo photo--round" role="img" aria-label="Salt and pepper calamari on a white plate" style="left:32px; top:555px; width:206px; height:206px; background:radial-gradient(circle,#e9c88c 0%,#c79a5a 80%);"></div>
    <div class="photo photo--round" role="img" aria-label="Sweet chili dipping sauce" style="left:259px; top:565px; width:86px; height:86px; border-width:8px; background:radial-gradient(circle,#e04a1e 0%,#b0260f 80%);"></div>
    <div class="photo photo--plate" role="img" aria-label="Vegetarian spring rolls with greens on a white plate" style="left:340px; top:560px; width:225px; height:180px; transform:rotate(5deg); background:linear-gradient(135deg,#4f7a2e 0%,#e3c27a 45%,#c99a55 100%);"></div>

    <article class="menu-item" style="left:221px; top:55px; width:160px;">
      <h3>Pork Egg Rolls (2)</h3>
      <p>Hand rolled with julienned veggies with our sweet n' sour mustard sauce</p>
    </article>

    <article class="menu-item" style="left:221px; top:107px; width:160px;">
      <h3>Beef Crispy Bottom Bao</h3>
      <p>Pan fried crispy bottom Bao, stuffed with beef, drizzled with scallion and sesame (Fresh made to order, takes at least 20 mins to serve)<span class="extra">add Shrimp $1</span></p>
    </article>
    <span class="chev chev--right" style="left:379px; top:120px;"></span>

    <span class="chev chev--up" style="left:94px; top:196px;"></span>
    <article class="menu-item" style="left:34px; top:207px; width:160px;">
      <h3>Crispy Mala Beef Jerky</h3>
      <p>Dry fried shredded beef with various peppers in sesame and peppercorn oil</p>
    </article>

    <article class="menu-item" style="left:36px; top:264px; width:150px;">
      <h3>Red Oil Dumplings (6)</h3>
      <p>Chicken filled dumplings in Sichuan red oil sauce drizzled with sesame</p>
    </article>
    <span class="chev chev--right" style="left:184px; top:275px;"></span>

    <article class="menu-item" style="left:202px; top:385px; width:150px;">
      <h3>Hot n' Sour Soup</h3>
      <p>Tangy broth with Bamboo shoot, wood ear mushrooms, tofu, egg and carrots</p>
    </article>
    <span class="chev chev--right" style="left:349px; top:396px;"></span>

    <span class="chev chev--left" style="left:190px; top:446px;"></span>
    <article class="menu-item" style="left:204px; top:441px; width:160px;">
      <h3>Lanternleaf Lettuce Wraps</h3>
      <p>Seasoned ground chicken drizzled with our top secret homemade sauce served with lettuce wraps</p>
    </article>

    <article class="menu-item" style="left:204px; top:510px; width:140px;">
      <h3>Salt &amp; Pepper Calamari</h3>
      <p>Crispy Calamari with Green &amp; red peppers and onions</p>
    </article>
    <span class="chev chev--down" style="left:207px; top:549px;"></span>

    <article class="menu-item" style="left:392px; top:509px; width:160px;">
      <h3>Vegetarian Spring Rolls (3)</h3>
      <p>Traditional Asian Roll served with a sweet chili sauce</p>
    </article>
    <span class="chev chev--down" style="left:458px; top:540px;"></span>
  </section>

</main>
</body>
</html>
```